a two sided flyer to advertise osteopathic/pilates business

we need a square format flyer that introduces our pilates business on one sided and our osteopathic business on the other.
we want the look an feel to be in rough keeping with some work we had done a while go and can be attached.

kelb osteopathy
BEAT PAIN
sports/spinal/pre+post natal
kelbclinic.com.au
94620381

kelb pilates
movement + strength
3 classes - $45
kelbclinic.com.au
94620381

Requirements
Must have
• 2 sided, consisten look and feel and a look and feel consistent with the kelb pilates png files attached
• charcoal/orange/white as a colour scheme

```html
<!DOCTYPE html>
<html lang="en">
<head>
<meta charset="utf-8">
<title>kelb osteopathy &amp; kelb pilates flyer</title>
<link rel="stylesheet" href="https://fonts.googleapis.com/css2?family=Poppins:wght@300;400;600;700&family=Oswald:wght@300;400&display=swap">
<style>
  :root {
    --charcoal: #2e2e2e;
    --charcoal-mid: #454545;
    --charcoal-soft: #5a5a5a;
    --orange: #f05a22;
    --orange-bright: #f26a30;
    --orange-soft: #f7936a;
    --peach: #f9a784;
    --white: #ffffff;
    --stage-edge: #8c7469;
    --stage-centre: #e9a48a;
  }
  html, body {
    margin: 0;
    padding: 0;
    width: 1200px;
    height: 720px;
    overflow: hidden;
  }
  body {
    background: radial-gradient(ellipse at center, var(--stage-centre) 0%, #c08a76 45%, var(--stage-edge) 100%);
    font-family: "Poppins", sans-serif;
    position: relative;
  }
  .flyer-side {
    position: absolute;
    top: 82px;
    width: 558px;
    height: 558px;
    box-shadow: 2px 3px 8px rgba(0, 0, 0, 0.45);
    border: 1px solid rgba(255, 255, 255, 0.6);
  }
  .flyer-side--osteopathy { left: 30px; }
  .flyer-side--pilates { left: 613px; }
  .flyer-side svg { display: block; width: 558px; height: 558px; }
  .label-condensed { font-family: "Oswald", sans-serif; font-weight: 300; }
  .headline-bold { font-family: "Poppins", sans-serif; font-weight: 700; }
  .body-light { font-family: "Poppins", sans-serif; font-weight: 300; }
  .body-bold { font-family: "Poppins", sans-serif; font-weight: 600; }
  .brand-name { font-family: "Poppins", sans-serif; font-weight: 600; }
</style>
</head>
<body>

<section class="flyer-side flyer-side--osteopathy" aria-label="kelb osteopathy side">
  <svg viewBox="0 0 558 558" xmlns="http://www.w3.org/2000/svg">
    <rect class="base" width="558" height="558" fill="var(--orange)"/>
    <path class="light-sweep" d="M250 0 H558 V330 C470 290 400 190 330 110 C300 70 275 35 250 0 Z" fill="var(--orange-soft)"/>
    <path class="corner-shape" d="M0 0 H250 C190 10 150 45 135 100 L0 100 Z" fill="var(--charcoal)"/>

    <circle class="corner-mark" cx="38" cy="38" r="21" fill="var(--white)" stroke="var(--orange)" stroke-width="5"/>
    <text class="brand-name" x="38" y="42" text-anchor="middle" font-size="11" fill="var(--charcoal)">kelb</text>
    <text class="label-condensed" x="80" y="34" font-size="11" fill="var(--white)">OSTEOPATHY</text>
    <text class="label-condensed" x="80" y="50" font-size="11" fill="var(--white)">CLINICAL PILATES</text>

    <rect class="title-band" x="178" y="93" width="380" height="57" fill="var(--white)"/>
    <text class="headline-bold" x="192" y="136" font-size="38" fill="var(--charcoal)">kelb <tspan fill="var(--orange)" font-weight="600">osteopathy</tspan></text>

    <polygon class="offer-panel" points="60,158 470,163 476,358 44,380" fill="var(--charcoal)" stroke="var(--peach)" stroke-width="5" stroke-linejoin="round"/>
    <text class="body-light" x="75" y="228" font-size="40" fill="var(--orange)">BEAT PAIN</text>
    <text class="body-light" x="75" y="260" font-size="22" fill="var(--white)">sports/spinal/pre+post natal</text>
    <text class="body-bold" x="75" y="292" font-size="22" fill="var(--white)">kelbclinic.com.au</text>
    <text class="headline-bold" x="75" y="340" font-size="36" fill="var(--orange)">94620381</text>

    <path class="footer-wave-light" d="M0 392 C180 375 380 412 558 388 V558 H0 Z" fill="var(--charcoal-mid)"/>
    <path class="footer-wave" d="M0 412 C200 400 380 430 558 400 V558 H0 Z" fill="var(--charcoal)"/>

    <circle class="footer-mark" cx="187" cy="487" r="40" fill="var(--white)" stroke="var(--orange)" stroke-width="9"/>
    <text class="brand-name" x="187" y="494" text-anchor="middle" font-size="20" fill="var(--charcoal)">kelb</text>
    <text class="label-condensed" x="270" y="481" font-size="24" fill="var(--white)">OSTEOPATHY</text>
    <text class="label-condensed" x="270" y="514" font-size="24" fill="var(--white)">CLINICAL PILATES</text>
  </svg>
</section>

<section class="flyer-side flyer-side--pilates" aria-label="kelb pilates side">
  <svg viewBox="0 0 558 558" xmlns="http://www.w3.org/2000/svg">
    <rect class="base" width="558" height="558" fill="var(--charcoal)"/>
    <path class="mid-sweep" d="M250 0 H558 V300 C470 260 400 170 330 100 C300 60 275 30 250 0 Z" fill="var(--charcoal-mid)"/>
    <path class="corner-shape" d="M0 0 H240 C185 12 150 45 140 95 L0 95 Z" fill="var(--charcoal)" stroke="var(--charcoal-soft)" stroke-width="1"/>

    <circle class="corner-mark" cx="38" cy="38" r="21" fill="var(--white)" stroke="var(--orange)" stroke-width="5"/>
    <text class="brand-name" x="38" y="42" text-anchor="middle" font-size="11" fill="var(--charcoal)">kelb</text>
    <text class="label-condensed" x="80" y="34" font-size="11" fill="var(--white)">OSTEOPATHY</text>
    <text class="label-condensed" x="80" y="50" font-size="11" fill="var(--white)">CLINICAL PILATES</text>

    <rect class="title-band" x="178" y="93" width="380" height="57" fill="var(--white)"/>
    <text class="headline-bold" x="192" y="136" font-size="38" fill="var(--charcoal)">kelb <tspan fill="var(--orange)" font-weight="600">pilates</tspan></text>

    <polygon class="offer-panel" points="44,160 472,162 478,376 42,378" fill="var(--orange-bright)" stroke="var(--charcoal-soft)" stroke-width="5" stroke-linejoin="round"/>
    <text class="body-light" x="72" y="205" font-size="29" fill="var(--white)">movement + strength</text>
    <text class="body-bold" x="72" y="242" font-size="24" fill="var(--white)">3 classes - $45</text>
    <text class="body-bold" x="72" y="278" font-size="24" fill="var(--white)">kelbclinic.com.au</text>
    <text class="headline-bold" x="72" y="332" font-size="38" fill="var(--charcoal)">94620381</text>

    <path class="footer-wave-light" d="M0 392 C180 378 380 408 558 384 V558 H0 Z" fill="var(--orange-soft)"/>
    <path class="footer-wave" d="M0 410 C200 398 380 428 558 398 V558 H0 Z" fill="var(--orange)"/>

    <rect class="figure-area" x="118" y="455" width="72" height="82" fill="var(--charcoal)" opacity="0.85" role="img" aria-label="Silhouette of a person standing beside a seated dog in front of an orange sun"/>
    <text class="brand-name" x="200" y="506" font-size="28" fill="var(--charcoal)">kelb</text>

    <circle class="brand-badge" cx="387" cy="485" r="50" fill="var(--charcoal)"/>
    <text class="brand-name" x="387" y="494" text-anchor="middle" font-size="26" fill="var(--white)">kelb</text>
  </svg>
</section>

</body>
</html>
```